TV - business card

Tidewell Vantage is an insurance brokerage firm, inovative, proactive, vigorous, which aims to become the leader of the insurance brokers in Anfrica. We should like to get some designs which should be avoided also in Gray / Metallic for the Administration and Orange / Blue for the Managers (ike in the picture sent). The Blue / Green logo is not the correct one, but the source of the file. Please adjust the color accordingly for the business cards. 1 / Orange / Blue 2 / Gray / Metallic We want something classic but which is transmitted strenght, inovation, modernity and most of all, rapidity. We want something start-up like, very punchy and catching eye remaining profesional at the same time. Name: Delton Ashgrove Function: Managing Director Address: N ° 73/74 Cmt. Bolembe - R / C 2B Esquerda - Bairro Quimbuta - Luanda Tel: (+244) 947 385 619 Email: delton.ashgrove@tidewell-v.com Website: www.tidewell-v. com We want classic in the front and creative, colorfull at the back. The cards will be printed in relief, with very high quality of paper.
Industry/Entity Type
Insurance Broker
Colors
Designer to choose colors to be used in the design.
Look and feel

```html
<!DOCTYPE html>
<html lang="en">
<head>
<meta charset="utf-8">
<title>Tidewell Vantage – Business Card</title>
<link href="https://fonts.googleapis.com/css2?family=Lato:wght@400;700;900&display=swap" rel="stylesheet">
<style>
  :root{
    --brand-blue:#1380c4;
    --brand-blue-deep:#0f6fae;
    --brand-orange:#ec7a1c;
    --paper:#f7f7f7;
    --ink:#1f1f1f;
    --stage:#d9d9d9;
    --faint-orange:#f6e3d3;
  }
  *{margin:0;padding:0;box-sizing:border-box}
  html,body{width:1200px;height:1021px;overflow:hidden;background:var(--stage)}
  body{font-family:"Lato",sans-serif;position:relative}
  .card{
    position:absolute;left:250px;width:700px;height:400px;overflow:hidden;
    box-shadow:0 10px 28px rgba(0,0,0,.25);
  }
  .card--front{top:90px;background:linear-gradient(135deg,var(--brand-blue),var(--brand-blue-deep))}
  .card--back{top:530px;background:var(--paper)}

  .front-ring{position:absolute;left:-40px;top:40px;width:320px;height:320px}
  .front-name{
    position:absolute;left:360px;top:182px;
    font-weight:900;font-size:30px;letter-spacing:1.5px;text-transform:uppercase;
    color:#fff;white-space:nowrap;
  }

  .back-ring{position:absolute;left:-120px;top:20px;width:420px;height:420px}
  .holder{position:absolute;left:70px;top:120px}
  .holder__name{font-weight:700;font-size:26px;color:var(--brand-blue)}
  .holder__role{font-size:18px;color:var(--ink);margin-top:2px}

  .company{position:absolute;left:380px;top:70px;width:290px}
  .company__mark{display:flex;align-items:center;gap:10px;margin-bottom:18px}
  .company__dot{width:34px;height:34px;border-radius:50%;background:var(--brand-orange)}
  .company__name{font-weight:900;font-size:20px;letter-spacing:.5px;text-transform:uppercase;color:var(--brand-orange);white-space:nowrap}
  .address{font-size:18px;line-height:1.3;color:var(--ink);margin-bottom:16px}
  .contacts{list-style:none;font-size:18px;color:var(--ink)}
  .contacts li{display:flex;align-items:center;gap:8px;line-height:1.45;white-space:nowrap}
  .contacts svg{width:16px;height:16px;flex:none}
</style>
</head>
<body>
  <section class="card card--front" aria-label="Card front">
    <svg class="front-ring" viewBox="0 0 320 320" aria-hidden="true">
      <circle cx="160" cy="160" r="146" fill="none" stroke="var(--brand-orange)" stroke-width="22"/>
    </svg>
    <div class="front-name">Tidewell Vantage</div>
  </section>

  <section class="card card--back" aria-label="Card back">
    <svg class="back-ring" viewBox="0 0 420 420" aria-hidden="true">
      <circle cx="210" cy="210" r="190" fill="none" stroke="var(--faint-orange)" stroke-width="30"/>
    </svg>
    <div class="holder">
      <div class="holder__name">Delton Ashgrove</div>
      <div class="holder__role">Managing Director</div>
    </div>
    <div class="company">
      <div class="company__mark">
        <span class="company__dot" aria-hidden="true"></span>
        <span class="company__name">Tidewell Vantage</span>
      </div>
      <p class="address">N ° 73/74 Cmt. Bolembe<br>R / C 2B Esquerda<br>Bairro Quimbuta - Luanda</p>
      <ul class="contacts">
        <li>
          <svg viewBox="0 0 16 16" aria-hidden="true"><path fill="var(--brand-orange)" d="M3.5 1l2.5 3-1.5 1.8c.9 1.9 2.3 3.3 4.2 4.2L10.5 8.5l3 2.5-1.5 3C6.5 14 2 9.5 1.5 3z"/></svg>
          (+244) 947 385 619
        </li>
        <li>
          <svg viewBox="0 0 16 16" aria-hidden="true"><rect x="1.5" y="3.5" width="13" height="9" fill="none" stroke="var(--brand-orange)" stroke-width="1.5"/><path d="M1.5 3.5l6.5 5 6.5-5" fill="none" stroke="var(--brand-orange)" stroke-width="1.5"/></svg>
          delton.ashgrove@tidewell-v.com
        </li>
        <li>
          <svg viewBox="0 0 16 16" aria-hidden="true"><g fill="none" stroke="var(--brand-orange)" stroke-width="1.3"><circle cx="8" cy="8" r="6.5"/><ellipse cx="8" cy="8" rx="3" ry="6.5"/><path d="M1.5 8h13M2.5 4.8h11M2.5 11.2h11"/></g></svg>
          www.tidewell-v.com
        </li>
      </ul>
    </div>
  </section>
</body>
</html>
```